Bref créative
DRK Business Card
Modern
Lou Ferrand
418B Quarry Gate Rd
Salisbury, MD 21801
lou@drkhvc.com
www.drkhvc.com
(see the bullet points on our existing business card and try to incorporate them)
Attached is our previous card. The services offered should be incorporated into the new card.
I can get an AI file of this logo if needed. Let me know.

```html
<!DOCTYPE html>
<html lang="en">
<head>
<meta charset="utf-8">
<title>DRK Stationery Set</title>
<link rel="stylesheet" href="https://fonts.googleapis.com/css2?family=Roboto:wght@400;700;900&display=swap">
<style>
  :root {
    --bg-dark: #2b2b2d;
    --bg-mid: #48484b;
    --paper: #ffffff;
    --brand: #1d3f9e;
    --brand-deep: #0d1f5c;
    --brand-light: #5d86d6;
    --ink: #4a4f5c;
    --faint: #e6e9f0;
    --flap-grey: #8d8f94;
  }
  * { box-sizing: border-box; margin: 0; padding: 0; }
  html, body { width: 1200px; height: 310px; overflow: hidden; }
  body {
    background: radial-gradient(ellipse at 50% 40%, var(--bg-mid), var(--bg-dark) 75%);
    font-family: "Roboto", Arial, sans-serif;
    position: relative;
  }
  .piece { position: absolute; background: var(--paper); overflow: hidden; box-shadow: 0 2px 5px rgba(0,0,0,.45); }
  .wave { position: absolute; left: 0; bottom: 0; width: 100%; }
  .brand-name { font-weight: 900; color: var(--brand); letter-spacing: -1px; display: flex; align-items: center; gap: 4px; line-height: 1; }
  .brand-dot { width: .42em; height: .42em; border-radius: 50%; background: var(--brand); display: inline-block; }
  .brand-faint { position: absolute; font-weight: 900; color: var(--faint); letter-spacing: -2px; line-height: 1; }
  .fine { font-size: 4px; color: var(--ink); line-height: 1.35; }

  /* master logo */
  .master-logo { position: absolute; left: 18px; top: 30px; }
  .master-logo .brand-name { font-size: 46px; color: #3c6ad0; }
  .master-logo .brand-dot { background: #3c6ad0; }
  .master-logo .tagline { font-size: 7px; color: #c9ccd4; margin-top: 3px; margin-left: 4px; }

  /* business cards */
  .card { width: 118px; height: 64px; }
  .card .brand-name { position: absolute; left: 7px; top: 7px; font-size: 17px; }
  .card .person { position: absolute; right: 7px; top: 9px; text-align: right; }
  .card .person strong { display: block; font-size: 6px; color: var(--brand-deep); }
  .card .details { position: absolute; right: 7px; top: 24px; text-align: right; }

  /* letterhead */
  .letterhead { width: 190px; height: 274px; top: 12px; }
  .letterhead .brand-name { position: absolute; left: 14px; top: 14px; font-size: 18px; }
  .letterhead .contact { position: absolute; right: 14px; top: 14px; text-align: right; }
  .letterhead .brand-faint { left: 28px; top: 95px; font-size: 62px; }
  .letterhead .footer { position: absolute; left: 0; right: 0; bottom: 5px; text-align: center; font-size: 3.5px; color: #fff; }

  /* landscape envelopes */
  .env-wide { width: 188px; height: 94px; left: 702px; }
  .env-wide .brand-name { position: absolute; left: 10px; top: 9px; font-size: 15px; }
  .env-wide .brand-faint { left: 98px; top: 30px; font-size: 34px; }
  .env-wide .return { position: absolute; left: 10px; top: 27px; }

  /* right envelopes */
  .env-right { width: 272px; height: 62px; left: 918px; }
  .flap { position: absolute; left: 0; top: 0; width: 100%; height: 100%; }
  .window { position: absolute; left: 28px; top: 22px; width: 92px; height: 26px; border: 1px solid #d5d8df; border-radius: 3px; }
</style>
</head>
<body>

<svg width="0" height="0" style="position:absolute" aria-hidden="true">
  <defs>
    <linearGradient id="band" x1="0" x2="1">
      <stop offset="0" stop-color="#0d1f5c"/>
      <stop offset=".6" stop-color="#1d3f9e"/>
      <stop offset="1" stop-color="#2f5cc0"/>
    </linearGradient>
    <symbol id="swoosh" viewBox="0 0 200 40" preserveAspectRatio="none">
      <path d="M0 22 C60 10 120 30 200 14 L200 40 L0 40 Z" fill="url(#band)"/>
      <path d="M0 20 C60 8 120 28 200 12 L200 15 C120 31 60 12 0 24 Z" fill="#9fb6e6"/>
      <path d="M0 30 C70 20 130 38 200 24" stroke="#5d86d6" stroke-width=".8" fill="none"/>
    </symbol>
  </defs>
</svg>

<div class="master-logo">
  <div class="brand-name"><span class="brand-dot"></span>DRK</div>
  <div class="tagline">Mechanical Services</div>
</div>

<!-- business cards -->
<div class="piece card" style="left:12px; top:130px;">
  <div class="brand-name">DRK</div>
  <div class="person fine"><strong>Lou Ferrand</strong>Service Manager</div>
  <svg class="wave" height="18"><use href="#swoosh"/></svg>
</div>
<div class="piece card" style="left:140px; top:130px;">
  <div class="brand-name">DRK</div>
  <div class="details fine">418B Quarry Gate Rd<br>Salisbury, MD 21801<br>lou@drkhvc.com<br>www.drkhvc.com</div>
  <svg class="wave" height="18"><use href="#swoosh"/></svg>
</div>
<div class="piece card" style="left:12px; top:208px;">
  <div class="brand-name">DRK</div>
  <div class="person fine"><strong>Lou Ferrand</strong>louaferrand</div>
  <svg class="wave" height="18"><use href="#swoosh"/></svg>
</div>
<div class="piece card" style="left:140px; top:208px;">
  <div class="brand-name">DRK</div>
  <div class="details fine">418B Quarry Gate Rd<br>Salisbury, MD 21801<br>lou@drkhvc.com<br>www.drkhvc.com</div>
  <svg class="wave" height="18"><use href="#swoosh"/></svg>
</div>

<!-- letterheads -->
<div class="piece letterhead" style="left:276px;">
  <div class="brand-name">DRK</div>
  <div class="contact fine">418B Quarry Gate Rd<br>Salisbury, MD 21801<br>lou@drkhvc.com</div>
  <div class="brand-faint">DRK</div>
  <svg class="wave" height="24"><use href="#swoosh"/></svg>
  <div class="footer">www.drkhvc.com</div>
</div>
<div class="piece letterhead" style="left:494px;">
  <div class="brand-name">DRK</div>
  <div class="contact fine">418B Quarry Gate Rd<br>Salisbury, MD 21801<br>lou@drkhvc.com</div>
  <div class="brand-faint">DRK</div>
  <svg class="wave" height="24"><use href="#swoosh"/></svg>
  <div class="footer">www.drkhvc.com</div>
</div>

<!-- wide envelopes -->
<div class="piece env-wide" style="top:38px;">
  <div class="brand-name">DRK</div>
  <div class="return fine">418B Quarry Gate Rd<br>Salisbury, MD 21801</div>
  <div class="brand-faint">DRK</div>
  <svg class="wave" height="20"><use href="#swoosh"/></svg>
</div>
<div class="piece env-wide" style="top:178px;">
  <div class="brand-name">DRK</div>
  <div class="return fine">418B Quarry Gate Rd<br>Salisbury, MD 21801</div>
  <div class="brand-faint">DRK</div>
  <svg class="wave" height="20"><use href="#swoosh"/></svg>
</div>

<!-- right envelopes -->
<div class="piece env-right" style="top:26px; background:#f2f3f5;">
  <svg class="flap" viewBox="0 0 272 62" preserveAspectRatio="none">
    <path d="M0 0 H272 V10 L136 34 L0 10 Z" fill="var(--flap-grey)"/>
  </svg>
</div>
<div class="piece env-right" style="top:100px;">
  <svg class="flap" viewBox="0 0 272 62" preserveAspectRatio="none">
    <path d="M0 0 H272 L136 40 Z" fill="url(#band)"/>
    <path d="M0 0 L136 40 L272 0" stroke="#9fb6e6" stroke-width="1.2" fill="none"/>
  </svg>
</div>
<div class="piece env-right" style="top:200px; height:72px;">
  <div class="window"></div>
  <svg class="wave" height="18"><use href="#swoosh"/></svg>
</div>

</body>
</html>
```